Retail Jewelry Business Card Design Project

We are in need of a new business card design for a retail jewelry store. This store is in the business of fine jewelry including but not specific to bridal jewelry, diamonds, designer jewelry and watches.

This store has been in business for 20 years but continues to strive for a modern professional appeal. The main colors use for this business are a royal blue, white and silver.

Target Market(s)

Target market is ages 18-50

Industry/Entity Type

Jewelry

Requirements
Must have
• Sales Person Name
Sales Person Email Address

Store Address
Store Phone
Website

Standard business card size. No odd shapes or sizes.
Nice to have
• Overall modern feel for card.

We have thought that a design with a nice feature of the logo on the back of the card would be nice but open to ideas.
Should not have
• No specific images of jewelry should be used.

```html
<!DOCTYPE html>
<html lang="en">
<head>
<meta charset="utf-8">
<title>Aldric Vale Fine Jewelry – Business Card</title>
<link rel="stylesheet" href="https://fonts.googleapis.com/css2?family=Crimson+Pro:wght@400;500&display=swap">
<style>
  :root {
    --page-bg: #eceef1;
    --card-paper: #d9dde3;
    --card-edge: #c3c8cf;
    --emboss-grey: #a3a8b0;
    --royal-blue: #2e2a9c;
    --ink: #1d1d22;
    --icon-blue: #3a3aa8;
  }
  * { box-sizing: border-box; margin: 0; padding: 0; }
  html, body {
    width: 1200px; height: 1000px; overflow: hidden;
    background: var(--page-bg);
    font-family: "Crimson Pro", Georgia, serif;
  }
  .sheet {
    position: relative; width: 1200px; height: 1000px;
  }
  .card {
    position: absolute;
    width: 560px; height: 336px;
    left: 320px;
    background: var(--card-paper);
    border: 1px solid var(--card-edge);
    box-shadow: 0 3px 10px rgba(0,0,0,0.12);
  }
  .card--front { top: 130px; }
  .card--back { top: 534px; }

  .front-brand {
    position: absolute; left: 0; right: 0; top: 120px;
    text-align: center;
    font-size: 64px; font-weight: 400;
    color: var(--emboss-grey);
    letter-spacing: 1px;
  }

  .back-brand {
    position: absolute; right: 32px; top: 24px;
    font-size: 50px; font-weight: 400;
    color: var(--royal-blue);
    line-height: 1;
  }

  .person { position: absolute; left: 46px; top: 166px; }
  .person__name { font-size: 21px; color: var(--ink); line-height: 1.1; letter-spacing: 0.5px; }
  .person__role { font-size: 14px; color: var(--royal-blue); margin-top: 2px; }

  .contacts {
    position: absolute; left: 22px; top: 220px;
    list-style: none;
  }
  .contacts__item {
    display: flex; align-items: center; gap: 9px;
    font-size: 13.5px; color: var(--ink);
    height: 18px;
  }
  .contacts__icon { width: 12px; height: 12px; fill: var(--icon-blue); flex: none; }
</style>
</head>
<body>
<main class="sheet">
  <section class="card card--front" aria-label="Card front">
    <p class="front-brand">Aldric Vale</p>
  </section>

  <section class="card card--back" aria-label="Card back">
    <p class="back-brand">Aldric Vale</p>

    <div class="person">
      <p class="person__name">Owen Harper</p>
      <p class="person__role">Sale Personnel</p>
    </div>

    <ul class="contacts">
      <li class="contacts__item">
        <svg class="contacts__icon" viewBox="0 0 12 12" aria-hidden="true"><path d="M3 1 L5 3.5 L4 5 Q5 7 7 8 L8.5 7 L11 9 L9.5 11 Q4 10.5 1 3 Z"/></svg>
        (555) 014 2286
      </li>
      <li class="contacts__item">
        <svg class="contacts__icon" viewBox="0 0 12 12" aria-hidden="true"><path d="M6 1 L11.5 6 L10 6 L10 11 L7.3 11 L7.3 7.8 L4.7 7.8 L4.7 11 L2 11 L2 6 L0.5 6 Z"/></svg>
        2280 Linden Avenue&nbsp; Bayport, FL 32499
      </li>
      <li class="contacts__item">
        <svg class="contacts__icon" viewBox="0 0 12 12" aria-hidden="true"><path d="M1 4 L6 1 L11 4 L11 10 L1 10 Z M1.8 4.4 L6 7 L10.2 4.4 L6 1.9 Z" fill-rule="evenodd"/></svg>
        Owen@aldricvalejewelry.com
      </li>
      <li class="contacts__item">
        <svg class="contacts__icon" viewBox="0 0 12 12" aria-hidden="true"><circle cx="6" cy="6" r="5"/><path d="M1 6 H11 M6 1 V11 M6 1 Q3 6 6 11 M6 1 Q9 6 6 11" stroke="#d9dde3" stroke-width="0.8" fill="none"/></svg>
        www.aldricvalejewelry.com
      </li>
    </ul>
  </section>
</main>
</body>
</html>
```